Security camera surveillance warning Sign

Security Camera Sign 11" x 11" Red, Yellow and Black (White Background)
I would like a line drawing of camera image attached.
Wording: All Suspicious or Criminal Activity Will Be Reported!
WARNING
24 HOUR SURVEILLANCE

Industry/Entity Type

Security

Colors
ec1f27
000000
ffc214

Requirements
Nice to have
• I uploaded a sign and would like the new design look something like that

```html
<!DOCTYPE html>
<html lang="en">
<head>
<meta charset="UTF-8">
<title>24 Hour Surveillance Warning Sign</title>
<link rel="stylesheet" href="https://fonts.googleapis.com/css2?family=Bebas+Neue&display=swap">
<style>
  :root {
    --sign-red: #e21f26;
    --sign-yellow: #fff200;
    --sign-black: #000000;
    --page-white: #ffffff;
  }
  html, body {
    margin: 0;
    padding: 0;
    width: 1200px;
    height: 1200px;
    overflow: hidden;
    background: var(--page-white);
  }
  .sign {
    display: block;
    width: 1200px;
    height: 1200px;
  }
  .sign-text {
    font-family: "Bebas Neue", "Oswald", sans-serif;
  }
  .headline { fill: var(--sign-yellow); }
  .body-text { fill: var(--sign-black); }
</style>
</head>
<body>
<svg class="sign" viewBox="0 0 1200 1200" xmlns="http://www.w3.org/2000/svg">
  <defs>
    <clipPath id="panel-shape">
      <rect x="45" y="45" width="1110" height="1105" rx="42" ry="42"/>
    </clipPath>
    <pattern id="hazard-stripes" patternUnits="userSpaceOnUse" width="44" height="62" patternTransform="skewX(-35)">
      <rect x="0" y="0" width="44" height="62" fill="var(--sign-yellow)"/>
      <rect x="0" y="0" width="20" height="62" fill="var(--sign-black)"/>
    </pattern>
    <linearGradient id="camera-tone" x1="0" y1="0" x2="1" y2="1">
      <stop offset="0" stop-color="#fff200"/>
      <stop offset="0.55" stop-color="#d9cc10"/>
      <stop offset="1" stop-color="#2a2a00"/>
    </linearGradient>
  </defs>

  <rect class="sign-frame" x="18" y="18" width="1164" height="1164" fill="var(--sign-black)"/>

  <g class="sign-panel" clip-path="url(#panel-shape)">
    <rect x="45" y="45" width="1110" height="1105" fill="var(--sign-yellow)"/>
    <rect class="header-band" x="45" y="45" width="1110" height="275" fill="var(--sign-red)"/>
    <rect class="hazard-band hazard-band--top" x="45" y="320" width="1110" height="62" fill="url(#hazard-stripes)"/>
    <rect class="hazard-band hazard-band--bottom" x="45" y="1108" width="1110" height="62" fill="url(#hazard-stripes)"/>
  </g>

  <text class="sign-text headline" x="175" y="280" font-size="275" textLength="855" lengthAdjust="spacingAndGlyphs">WARNING!</text>

  <path class="camera-illustration" role="img" aria-label="Line drawing of a wall-mounted security camera on its bracket"
        d="M365 455 Q365 400 420 400 H1090 Q1145 400 1145 455 V885 Q1145 940 1090 940 H825 Q770 940 770 885 V745 H420 Q365 745 365 690 Z"
        fill="url(#camera-tone)"/>

  <text class="sign-text body-text hours" x="88" y="895" font-size="185" textLength="467" lengthAdjust="spacingAndGlyphs">24 HOUR</text>
  <text class="sign-text body-text surveillance" x="88" y="985" font-size="107" textLength="467" lengthAdjust="spacingAndGlyphs">SURVEILLANCE</text>
  <text class="sign-text body-text notice" x="88" y="1085" font-size="57" textLength="1027" lengthAdjust="spacingAndGlyphs">ALL SUSPICIOUS OR CRIMINAL ACTIVITY WILL BE REPORTED!</text>
</svg>
</body>
</html>
```